Flyer-Design für Betreuung von pflegebedürftigen/hilfebedürftigen Senioren
Ich bin begeistert! Sehr gute und geduldige Bearbeitung meiner Änderungswünsche. Gute und schnelle Kommunikation. Danke!
Zielgruppe
Alltagshilfe, Betreuung, Begleitung und Unterstützung von pflegebedürftigen/hilfebedürftigen Senioren
Wir begleiten Senioren im Alltag, in Ihrer Freizeit, zu Ausflügen und Veranstaltungen, oder einfach mal zum Kaffee trinken. Wir erledigen Einkäufe, unterstützen bei Arzt und Behördengängen oder haben einfach nur ein offenes Ohr und schenken unsere Zeit. Gesellschaftsspiele, Gedächtnistraining und Erinnerungspflege für die kognitive Aktivierung kommen unter anderem bei den betreuen Demenzkranken zum Einsatz. Auch die physische Aktivierung in Form von Spaziergängen oder Bewegungsübungen gehört zum Arbeitsalltag.
Wir betreuuen die Senioren stundenweise im eigenen häuslichen Umfeld. Dadurch werden deren pflegende Angehörige entlastet und der Senior dabei unterstützt, seine Eigenständigkeit zu erhalten.
Aufgabenstellung
Nach Möglichkeit hätte ich gern Bilder eingebunden, auf denen keine Menschen sondern eher Figuren zu sehen sind, welche Liebe, Zusammenhalt, Familie und Unterstützung suggerieren, ähnlich wie bei dem Beispielflyer den ich mit hochlade. Die Schrift sollte Seniorengerecht und evtl. in Anlehnung an das Logo sein (Lindauer Altenbeistand - Helvetica Neue - 43 Light Extended / Slogan - Lato - Bold ). Die Farben des Logos, welche sich gern im Flyer wiederfinden dürfen sind: Rot: #BA2428 ; Orange: #F26C21
Vielleicht könnte man Puzzleteile kreativ einarbeiten? Senioren- und Alltagsbegleitung im häuslichen Umfeld ist ja einer von mehreren Bausteinen (neben Pflegedienst ect) der die Angehörigen entlastet und die Senioren unterstützt um den Alltag solange wie möglich in den eigenen 4 Wänden zu organisieren.. Allerdings kein Muss, nur ein Gedanke.
Auch bezüglich des Textes bin ich noch nicht 100% sicher. Gibt es die Möglichkeit, ein Vorgesehenes Textfeld nach dem Erwerb des Designs selbst zu ändern? Am besten mit Microsoft Word, oder so?

```html
<!DOCTYPE html>
<html lang="de">
<head>
<meta charset="utf-8">
<title>Lindauer Altenbeistand – Faltblatt</title>
<link href="https://fonts.googleapis.com/css2?family=Lato:wght@300;400;700;900&display=swap" rel="stylesheet">
<style>
  :root{
    --red:#ba2428;
    --red-deep:#ad1d24;
    --orange:#f26c21;
    --orange-warm:#e8641f;
    --tick:#d9411f;
    --text:#3e3e3e;
    --muted:#5a5a5a;
    --page:#e2e3e5;
    --rule:#d9d9d9;
    --band:linear-gradient(90deg,var(--red-deep) 0%,var(--orange-warm) 33%,var(--red-deep) 66.6%,var(--orange) 84%,var(--red-deep) 100%);
    --title:linear-gradient(90deg,var(--red) 0%,var(--orange) 100%);
  }
  *{box-sizing:border-box;margin:0;padding:0}
  html,body{width:813px;height:1200px;overflow:hidden}
  body{background:var(--page);font-family:"Lato",sans-serif;color:var(--text);position:relative}

  .sheet{position:absolute;left:47.5px;width:716px;height:510px;background:var(--band);box-shadow:0 10px 22px rgba(0,0,0,.12);overflow:hidden}
  .sheet--outside{top:46px}
  .sheet--inside{top:611px}
  .sheet__paper{position:absolute;inset:0;width:716px;height:510px}
  .fold{position:absolute;top:16px;width:1px;background:var(--rule)}

  .abs{position:absolute}
  .panel-title{position:absolute;font-weight:900;font-size:21px;line-height:1;letter-spacing:-.2px;white-space:nowrap}
  .panel-title .dark{color:var(--red)}
  .panel-title .warm{color:#d9411f}

  .quote{position:absolute;font-size:8px;font-weight:400;line-height:10.35px;color:var(--text);white-space:nowrap}
  .quote--left{text-align:left}
  .quote--right{text-align:right}
  .quote-mark{position:absolute;font-weight:900;font-size:14px;line-height:1;color:var(--tick)}

  .photo-disc{position:absolute;border-radius:50%;border:1.5px solid var(--orange);background:radial-gradient(circle at 35% 40%,#d7a78c 0%,#c7957a 30%,#a9a777 62%,#7f8f58 100%)}
  .icon-spot{position:absolute;border-radius:6px;background:var(--orange);opacity:.85}

  .checklist{position:absolute;list-style:none;font-size:10.4px;line-height:12.4px;color:var(--text)}
  .checklist li{position:relative;padding-left:18px;margin-bottom:11.9px}
  .checklist li::before{content:"";position:absolute;left:2px;top:-1px;width:5px;height:10px;border-right:2.2px solid var(--tick);border-bottom:2.2px solid var(--tick);transform:rotate(38deg)}
  .checklist--tight li{padding-left:15px}

  .fine-print{position:absolute;left:255px;top:370px;font-size:6.4px;line-height:8px;font-weight:700;color:var(--muted)}

  .contact{position:absolute;left:238px;width:239px;text-align:center;color:#fff;font-weight:700;font-size:9px;line-height:11px;white-space:nowrap}
  .contact--firm{font-size:8.8px;line-height:11px;text-transform:uppercase}

  .brand{position:absolute;left:505px;top:36px;width:200px}
  .brand__mark{position:absolute;left:0;top:8px;width:30px;height:30px;border-radius:50%;border:2px solid var(--orange)}
  .brand__name{position:absolute;left:38px;top:0;font-weight:300;font-size:17.5px;line-height:17px;color:var(--orange)}
  .brand__owner{position:absolute;left:38px;top:38px;font-weight:300;font-size:9.5px;color:var(--orange);white-space:nowrap}
  .slogan{position:absolute;left:477px;width:239px;top:93px;text-align:center;font-weight:700;font-size:6.3px;letter-spacing:1.9px;color:var(--red)}

  .cover-head{position:absolute;left:477px;width:239px;top:410px;text-align:center;color:#fff;font-weight:900;font-size:20px;line-height:22.5px}
  .cover-url{position:absolute;left:477px;width:239px;top:484px;text-align:center;color:#fff;font-weight:700;font-size:9.4px}

  .inside-title{position:absolute;width:239px;top:86px;text-align:center;font-weight:900;font-size:22px;line-height:1;letter-spacing:.2px;background:var(--title);-webkit-background-clip:text;background-clip:text;color:transparent}
  .inside-copy{position:absolute;width:205px;top:84px;text-align:center;font-size:8px;line-height:10.3px;color:var(--text)}
  .inside-copy b{color:var(--orange);font-weight:700}

  .cta{position:absolute;width:239px;text-align:center;color:#fff;font-weight:700;font-size:13.2px;line-height:16.5px}
</style>
</head>
<body>

<section class="sheet sheet--outside">
  <svg class="sheet__paper" viewBox="0 0 716 510" aria-hidden="true">
    <path fill="#fff" d="M0,45 C55,20 150,16 238,16 L680,16 C702,16 716,22 716,28 L716,398 C680,399 620,401 570,402 C525,398 488,350 477,293 C462,365 400,410 300,412 L238,414 L238,510 L0,510 Z"/>
    <g stroke="var(--orange)" stroke-width=".8" stroke-dasharray="1.5 2" fill="none">
      <line x1="597" y1="188" x2="597" y2="170"/>
      <line x1="597" y1="314" x2="597" y2="335"/>
      <line x1="534" y1="251" x2="514" y2="251"/>
      <line x1="660" y1="251" x2="680" y2="251"/>
      <line x1="552" y1="206" x2="538" y2="192"/>
      <line x1="642" y1="206" x2="656" y2="192"/>
      <line x1="552" y1="296" x2="538" y2="310"/>
      <line x1="642" y1="296" x2="656" y2="310"/>
    </g>
  </svg>
  <div class="fold" style="left:238px;height:398px"></div>
  <div class="fold" style="left:477px;height:278px"></div>

  <h2 class="panel-title" style="left:18.5px;top:44px"><span class="dark">Unsere </span><span class="warm">Referenzen</span></h2>

  <span class="quote-mark" style="left:18px;top:82px">“</span>
  <p class="quote quote--left" style="left:31px;top:81px">
    Lorem ipsumObis moluptus.<br>Apiduciendae voluptatem<br>labore diost, omnisimet<br>repellande num res dellut<br>litate offic tempero reperes<br>restior enditas re ped<br>quis estia nonsent uteceri<br>officiamet accusam, nobissit ut as restis sum<br>sim explate pro voluptati idel es rem.
  </p>
  <div class="photo-disc" role="img" aria-label="Foto: ältere Hand ruht in einer helfenden Hand" style="left:144px;top:82px;width:64px;height:64px"></div>

  <span class="quote-mark" style="left:193px;top:196px">“</span>
  <p class="quote quote--right" style="right:527px;top:195px">
    Lorem ipsumObis moluptus.<br>Apiduciendae voluptatem labore diost,<br>omnisimet repellande num res dellut litate<br>offic tempero reperes restior enditas re<br>ped quis estia nonsent uteceri officiamet<br>accusam, nobissit ut volorum nus as restis<br>sum sim explate pro voluptati idel es rem.
  </p>

  <span class="quote-mark" style="left:18px;top:289px">“</span>
  <p class="quote quote--left" style="left:31px;top:288px">
    Lorem ipsumObis moluptus.<br>Apiduciendae voluptatem labore diost,<br>omnisimet repellande num res dellut litate<br>offic tempero reperes restior enditas re<br>ped quis estia nonsent uteceri officiamet<br>accusam, nobissit ut volorum nus as restis<br>sum sim explate pro voluptati idel es rem.
  </p>

  <span class="quote-mark" style="left:193px;top:383px">“</span>
  <p class="quote quote--right" style="right:527px;top:382px">
    Lorem ipsumObis<br>moluptus. Apiduciendae<br>voluptatem labore diost,<br>omnisimet repellande<br>num res dellut litate offic<br>tempero reperes restior<br>enditas re ped quis estia<br>nonsent uteceri officiamet accusam,<br>nobissit ut volorum nus as restis sum sim<br>explate pro voluptati idel es rem.
  </p>
  <div class="photo-disc" role="img" aria-label="Foto: ältere Hand ruht in einer helfenden Hand" style="left:27px;top:387px;width:64px;height:64px"></div>

  <h2 class="panel-title" style="left:255px;top:44px"><span class="dark">Unsere </span><span class="warm">Leistungen</span></h2>
  <ul class="checklist" style="left:255px;top:83px;width:220px">
    <li>Unterstützung bei der Alltagsgestaltung</li>
    <li>Begleitung zum Einkauf und<br>zu Ärzten/Behörden</li>
    <li>Beratung bei allgemeinen Fragen</li>
    <li>Besuch von Veranstaltungen,<br>Museen, Theater</li>
    <li>Ausflüge (z.B. Zoobesuch)</li>
    <li>Entlastung von pflegenden Angehörigen</li>
    <li>Körperliche Aktivierung, z.B. Spaziergänge</li>
    <li>Gespräche über aktuelle Themen<br>und Vergangenes</li>
    <li>Erinnerungspflege/Biographiearbeit</li>
    <li>Gesellschaft leisten und Zeit schenken</li>
  </ul>
  <p class="fine-print">Die Kostenübernahme ist bei<br>bestehendem Pflegegrad<br>durch die Pflegekasse möglich.</p>

  <p class="contact contact--firm" style="top:427px">Lindauer Altenbeistand<br>Hanne Folmerit</p>
  <p class="contact" style="top:456px">Lindenweg 12 · 88131 Lindau</p>
  <p class="contact" style="top:472px">Tel.: 0170 55 01 234</p>
  <p class="contact" style="top:488px">info@lindauer-altenbeistand.de</p>

  <div class="brand">
    <span class="brand__mark"></span>
    <span class="brand__name">Lindauer<br>Altenbeistand</span>
    <span class="brand__owner">Inh. Hanne Folmerit</span>
  </div>
  <p class="slogan">BEGLEITUNG-BETREUUNG-WERTSCHÄTZUNG</p>

  <div class="photo-disc" role="img" aria-label="Foto: ältere Hand liegt in einer stützenden Hand" style="left:533px;top:187px;width:128px;height:128px;outline:1.5px solid var(--orange);outline-offset:3px"></div>
  <span class="icon-spot" role="img" aria-label="Symbol Schaukelstuhl" style="left:587px;top:150px;width:20px;height:18px"></span>
  <span class="icon-spot" role="img" aria-label="Symbol Wollknäuel" style="left:652px;top:172px;width:18px;height:18px;border-radius:50%"></span>
  <span class="icon-spot" role="img" aria-label="Symbol Rollstuhl" style="left:520px;top:166px;width:22px;height:22px"></span>
  <span class="icon-spot" role="img" aria-label="Symbol Brille" style="left:680px;top:244px;width:26px;height:11px"></span>
  <span class="icon-spot" role="img" aria-label="Symbol älteres Paar" style="left:488px;top:238px;width:24px;height:26px"></span>
  <span class="icon-spot" role="img" aria-label="Symbol Haus" style="left:512px;top:308px;width:28px;height:18px"></span>
  <span class="icon-spot" role="img" aria-label="Symbol Baum" style="left:590px;top:335px;width:13px;height:22px;border-radius:6px 6px 2px 2px"></span>
  <svg class="abs" style="left:655px;top:308px" width="24" height="22" viewBox="0 0 24 22" aria-label="Telefon" role="img">
    <rect x="6" y="1" width="17" height="20" rx="2.5" fill="var(--orange)"/>
    <rect x="8.5" y="3" width="4" height="16" rx="1" fill="#fff"/>
    <g fill="#fff"><rect x="14" y="5" width="2" height="2"/><rect x="17.5" y="5" width="2" height="2"/><rect x="14" y="9" width="2" height="2"/><rect x="17.5" y="9" width="2" height="2"/><rect x="14" y="13" width="2" height="2"/><rect x="17.5" y="13" width="2" height="2"/></g>
    <path d="M6 5 C2 5 1 8 1 11 C1 15 2 18 6 18" stroke="var(--orange)" stroke-width="1.4" fill="none"/>
  </svg>

  <h1 class="cover-head">Dienstleistungen<br>für Senioren und den<br>Alltag in Lindau</h1>
  <p class="cover-url">www.lindauer-altenbeistand.de</p>
</section>

<section class="sheet sheet--inside">
  <svg class="sheet__paper" viewBox="0 0 716 510" aria-hidden="true">
    <path fill="#fff" d="M0,45 C55,20 150,16 238,16 L680,16 C702,16 716,22 716,28 L716,373 C690,420 600,450 477,454 L238,458 L0,460 Z"/>
  </svg>
  <div class="fold" style="left:238px;height:442px"></div>
  <div class="fold" style="left:477px;height:438px"></div>

  <h2 class="inside-title" style="left:0;top:44px">BEGLEITUNG</h2>
  <p class="inside-copy" style="left:16.5px">Lorem ipsumObis moluptus. <b>Apiduciendae</b> voluptatem labore diost, omnisimet repellande num res dellut litate offic tempero reperes restior enditas re ped quis estia nonsent <b>uteceri</b> officiamet accusam, nobissit ut as restis sum sim explate pro voluptati idel es rem. Commolupta providitem et volorem quias.</p>
  <div class="photo-disc" role="img" aria-label="Foto: gehaltene Hände" style="left:15px;top:187px;width:63px;height:63px"></div>
  <div class="photo-disc" role="img" aria-label="Foto: gehaltene Hände" style="left:153px;top:187px;width:63px;height:63px"></div>
  <div class="photo-disc" role="img" aria-label="Foto: gehaltene Hände" style="left:84px;top:239px;width:63px;height:63px"></div>
  <span class="icon-spot" role="img" aria-label="Grafik: älteres Paar mit Gehstöcken" style="left:88px;top:162px;width:48px;height:54px;border-radius:10px"></span>
  <ul class="checklist checklist--tight" style="left:25px;top:319px;width:210px">
    <li>Zum Einkauf und zu Ärzten/Behörden</li>
    <li>Beratung bei allgemeinen Fragen</li>
    <li>Zu Veranstaltungen, Museen, Theater</li>
    <li>Zu Ausflügen (z.B. Zoobesuch)</li>
    <li>Zu körperlicher Betätigung</li>
  </ul>

  <h2 class="inside-title" style="left:238px;top:44px">BETREUUNG</h2>
  <p class="inside-copy" style="left:255.5px">Lorem ipsumObis moluptus. <b>Apiduciendae</b> voluptatem labore diost, omnisimet repellande num res dellut litate offic tempero reperes restior enditas re ped quis estia nonsent <b>uteceri</b> officiamet accusam, nobissit ut as restis sum sim explate pro voluptati idel es rem. Commolupta providitem et volorem quias.Sat. Hos, corum or hos fac reo, consum et intene escipse dicati coente inum Romnentemus, non ductus; esimius cipimus, Catis clatra, Catquo acturem is, cone auderius rei in dius effrehe busque remus firit, ut ve,Cente, populin cescid pubit, elibus, unum ommodi, cem sperum deris Maectam privivici sed fac mod.</p>
  <svg class="abs" style="left:333px;top:223px" width="46" height="46" viewBox="0 0 24 22" role="img" aria-label="Telefon">
    <rect x="6" y="1" width="17" height="20" rx="2.5" fill="var(--orange)"/>
    <rect x="8.5" y="3" width="4" height="16" rx="1" fill="#fff"/>
    <g fill="#fff"><rect x="14" y="5" width="2" height="2"/><rect x="17.5" y="5" width="2" height="2"/><rect x="14" y="9" width="2" height="2"/><rect x="17.5" y="9" width="2" height="2"/><rect x="14" y="13" width="2" height="2"/><rect x="17.5" y="13" width="2" height="2"/></g>
    <path d="M6 5 C2 5 1 8 1 11 C1 15 2 18 6 18" stroke="var(--orange)" stroke-width="1" fill="none"/>
  </svg>
  <ul class="checklist checklist--tight" style="left:254px;top:289px;width:215px">
    <li>Unterstützung bei der Alltagsgestaltun</li>
    <li>Beratung bei allgemeinen Fragen</li>
    <li>Entlastung von pflegenden Angehörigen</li>
  </ul>
  <div class="photo-disc" role="img" aria-label="Foto: gehaltene Hände" style="left:250px;top:368px;width:63px;height:63px"></div>
  <div class="photo-disc" role="img" aria-label="Foto: gehaltene Hände" style="left:324px;top:368px;width:63px;height:63px"></div>
  <div class="photo-disc" role="img" aria-label="Foto: gehaltene Hände" style="left:397px;top:368px;width:63px;height:63px"></div>

  <h2 class="inside-title" style="left:477px;top:44px">WERTSCHÄTZUNG</h2>
  <p class="inside-copy" style="left:494.5px">Lorem ipsumObis moluptus. <b>Apiduciendae</b> voluptatem labore diost, omnisimet repellande num res dellut litate offic tempero reperes restior enditas re ped quis estia nonsent <b>uteceri</b> officiamet accusam, nobissit ut as restis sum sim explate pro voluptati idel es rem. Commolupta providitem et volorem quias.</p>
  <div class="photo-disc" role="img" aria-label="Foto: gehaltene Hände" style="left:565px;top:161px;width:63px;height:63px"></div>
  <div class="photo-disc" role="img" aria-label="Foto: gehaltene Hände" style="left:496px;top:219px;width:63px;height:63px"></div>
  <div class="photo-disc" role="img" aria-label="Foto: gehaltene Hände" style="left:633px;top:219px;width:63px;height:63px"></div>
  <span class="icon-spot" role="img" aria-label="Grafik: Schaukelstuhl" style="left:572px;top:250px;width:50px;height:44px;border-radius:8px"></span>
  <ul class="checklist checklist--tight" style="left:494px;top:319px;width:215px">
    <li>Gespräche über aktuelle Themen<br>und Vergangenes</li>
    <li>Erinnerungspflege/Biographiearbeit</li>
    <li>Gesellschaft leisten<br>und Zeit schenken</li>
  </ul>

  <p class="cta" style="left:0;top:490px">Jetzt alle Leistungen entdecken</p>
  <p class="cta" style="left:238px;top:490px">und unverbindlich informieren</p>
  <p class="cta" style="left:477px;top:473px">unter www.lindauer-<br>altenbeistand.de</p>
</section>

</body>
</html>
```